Brimovex business card

Based on company logo and website given , to design a business card temple. Slogan "Your furry friends deserves the best"
Color style please refer to our website

```html
<!DOCTYPE html>
<html lang="en">
<head>
<meta charset="utf-8">
<title>Brimovex Business Card</title>
<link rel="stylesheet" href="https://fonts.googleapis.com/css2?family=Mulish:wght@400;800&family=Courgette&display=swap">
<style>
  :root {
    --backdrop: #c9c9c9;
    --forest-deep: #0e2a22;
    --forest-mid: #27493a;
    --forest-light: #4a6a4c;
    --earth: #5c5a44;
    --gold: #bcb33a;
    --pine: #0a2e28;
    --leaf: #1d6a3e;
    --ink: #2a2a2a;
    --paper: #ffffff;
    --badge-green: #1f7a3d;
    --badge-gold: #d6b24a;
    --badge-red: #c4252d;
  }
  * { box-sizing: border-box; margin: 0; padding: 0; }
  html, body { width: 1200px; height: 900px; overflow: hidden; }
  body {
    background: var(--backdrop);
    font-family: "Mulish", sans-serif;
    position: relative;
  }
  .card {
    position: absolute;
    left: 250px;
    width: 700px;
    height: 400px;
    overflow: hidden;
    box-shadow: 0 6px 18px rgba(0,0,0,0.25);
  }
  .card--front { top: 40px; }
  .card--back { top: 460px; background: var(--paper); }

  /* Front */
  .front__scene {
    position: absolute; inset: 0;
    background:
      radial-gradient(ellipse 22% 30% at 50% 48%, #7a6a3e 0%, rgba(122,106,62,0) 100%),
      radial-gradient(ellipse 60% 40% at 50% 95%, var(--earth) 0%, rgba(92,90,68,0) 100%),
      linear-gradient(90deg, var(--forest-mid) 0%, var(--forest-deep) 35%, var(--forest-deep) 60%, var(--forest-light) 100%);
  }
  .front__slogan {
    position: absolute; top: 62px; left: 0; right: 0;
    text-align: center;
    font-family: "Courgette", cursive;
    color: var(--paper);
    font-size: 24px;
  }
  .front__brand {
    position: absolute; bottom: 58px; left: 0; right: 0;
    text-align: center;
    font-weight: 800;
    font-size: 64px;
    color: var(--gold);
    letter-spacing: 1px;
  }
  .badge { position: absolute; border-radius: 50%; }
  .badge--green {
    left: 48px; bottom: 34px; width: 92px; height: 92px;
    background: var(--badge-green); border: 6px solid var(--paper);
  }
  .badge--gold {
    right: 70px; top: 180px; width: 96px; height: 96px;
    background: var(--badge-gold); border: 4px solid #e9cf78;
  }
  .badge--gold::after {
    content: ""; position: absolute; left: -14px; right: -14px; top: 34px; height: 22px;
    background: var(--badge-red);
  }

  /* Back */
  .back__brand {
    position: absolute; top: 46px; left: 52px;
    font-weight: 800; font-size: 50px; color: var(--gold);
  }
  .back__person { position: absolute; top: 142px; left: 56px; }
  .back__name { font-weight: 800; font-size: 24px; color: var(--leaf); }
  .back__role { font-size: 19px; color: var(--ink); }
  .back__address {
    position: absolute; top: 222px; left: 56px;
    font-style: normal; font-size: 19px; color: var(--ink); line-height: 1.3;
  }
  .back__contacts {
    position: absolute; top: 284px; left: 40px;
    list-style: none; font-size: 19px; color: var(--ink); line-height: 1.35;
  }
  .back__contacts li { display: flex; align-items: center; gap: 8px; }
  .back__contacts svg { width: 16px; height: 16px; flex: none; }
  .back__block {
    position: absolute; right: 0; bottom: 0; width: 300px; height: 330px;
    background: var(--pine);
    border-top-left-radius: 60px;
  }
</style>
</head>
<body>
  <section class="card card--front">
    <div class="front__scene" role="img" aria-label="Photograph of a dog sitting on a forest path among ferns"></div>
    <p class="front__slogan">Your furry friends deserves the best</p>
    <div class="badge badge--gold" role="img" aria-label="Product badge"></div>
    <div class="badge badge--green" role="img" aria-label="Product badge"></div>
    <p class="front__brand">Brimovex</p>
  </section>

  <section class="card card--back">
    <p class="back__brand">Brimovex</p>
    <div class="back__person">
      <p class="back__name">Daniel Hartley</p>
      <p class="back__role">Founder / Owner</p>
    </div>
    <address class="back__address">12/48 Ashgrove Lane<br>Hillcrest Vic 3150</address>
    <ul class="back__contacts">
      <li>
        <svg viewBox="0 0 16 16" fill="none" stroke="#1d6a3e" stroke-width="1.5"><rect x="4" y="1" width="8" height="14" rx="1.5"/><line x1="7" y1="12.5" x2="9" y2="12.5"/></svg>
        +61 03 9000 1234
      </li>
      <li>
        <svg viewBox="0 0 16 16" fill="#1d6a3e"><path d="M3 1.5l3 .5 1 3.5-2 1.2a8 8 0 0 0 4.3 4.3l1.2-2 3.5 1 .5 3c-.5 1-1.5 1.5-2.5 1.5C6.5 14.5 1.5 9.5 1.5 4c0-1 .5-2 1.5-2.5z"/></svg>
        1800 000 111
      </li>
      <li>
        <svg viewBox="0 0 16 16" fill="none" stroke="#1d6a3e" stroke-width="1.5"><rect x="1" y="3" width="14" height="10"/><polyline points="1,3 8,9 15,3"/></svg>
        info@brimovex.com.au
      </li>
      <li>
        <svg viewBox="0 0 16 16" fill="none" stroke="#1d6a3e" stroke-width="1.3"><circle cx="8" cy="8" r="6.5"/><ellipse cx="8" cy="8" rx="3" ry="6.5"/><line x1="1.5" y1="8" x2="14.5" y2="8"/></svg>
        www.brimovex.com.au
      </li>
    </ul>
    <div class="back__block"></div>
  </section>
</body>
</html>
```